HomeBridle business card and stationary design

We are looking for a simple yet elegant design for our mortgage company business card and stationary.

The card should include:
Name (Derek Walsh)
Title (CEO)
Phone Number (614-208-3917)
Address (48 Birchfield Court, Suite 314, Marlow, OH 43952)
Email (email@homebridle-example.com)
"NMLS" i.e. (NMLS 61947)
"Company NMLS" (Company NMLS 472815)

See above

```html
<!DOCTYPE html>
<html lang="en">
<head>
<meta charset="utf-8">
<title>HomeBridle — Business Card Set</title>
<link href="https://fonts.googleapis.com/css2?family=Montserrat:wght@400;500;700;800&display=swap" rel="stylesheet">
<style>
  :root {
    --brand-blue: #27abe2;
    --ink: #1b2430;
    --paper: #ffffff;
    --page: #ffffff;
    --shadow: rgba(80, 120, 170, 0.22);
  }
  * { box-sizing: border-box; margin: 0; padding: 0; }
  html, body {
    width: 1200px;
    height: 1200px;
    overflow: hidden;
    background: var(--page);
    font-family: "Montserrat", Arial, sans-serif;
  }
  .card-set {
    position: relative;
    width: 1200px;
    height: 1200px;
  }
  .card {
    position: absolute;
    width: 534px;
    height: 321px;
    box-shadow: 0 4px 10px var(--shadow);
    overflow: hidden;
  }
  .card--light { background: var(--paper); color: var(--ink); }
  .card--blue { background: var(--brand-blue); color: var(--paper); }

  .card--front-light { left: 49px; top: 275px; }
  .card--front-blue  { left: 625px; top: 275px; }
  .card--back-light  { left: 49px; top: 612px; }
  .card--back-blue   { left: 625px; top: 612px; }

  /* Front side */
  .contact {
    position: absolute;
    left: 297px;
    top: 62px;
  }
  .contact__name {
    font-weight: 800;
    font-size: 19.5px;
    letter-spacing: 0.2px;
    line-height: 1;
    text-transform: uppercase;
    white-space: nowrap;
  }
  .card--light .contact__surname { color: var(--brand-blue); }
  .card--blue .contact__surname { color: var(--ink); }
  .contact__title {
    margin-top: 9px;
    font-size: 11px;
    font-weight: 500;
    letter-spacing: 3px;
  }
  .contact__rule {
    width: 20px;
    height: 1px;
    margin-top: 30px;
    margin-bottom: 4px;
  }
  .card--light .contact__rule { background: var(--brand-blue); }
  .card--blue .contact__rule { background: var(--ink); }
  .contact__details {
    list-style: none;
    font-size: 12.2px;
    font-weight: 400;
    line-height: 16px;
  }
  .contact__details li { margin-bottom: 2px; white-space: nowrap; }
  .company-license {
    position: absolute;
    left: 297px;
    top: 264px;
    font-size: 12.2px;
    font-weight: 400;
    white-space: nowrap;
  }

  .wordmark {
    position: absolute;
    display: flex;
    align-items: center;
    font-weight: 600;
    white-space: nowrap;
    line-height: 1;
  }
  .card--light .wordmark { color: var(--brand-blue); }
  .card--blue .wordmark { color: var(--paper); }

  .wordmark--small {
    left: 37px;
    top: 252px;
    font-size: 25px;
    gap: 8px;
  }
  .wordmark--small .wordmark__dot { width: 12px; height: 12px; }

  .wordmark--large {
    left: 0;
    right: 0;
    top: 0;
    bottom: 0;
    justify-content: center;
    font-size: 60px;
    gap: 18px;
    padding-top: 22px;
  }
  .wordmark--large .wordmark__dot { width: 26px; height: 26px; }

  .wordmark__dot {
    display: inline-block;
    border-radius: 50%;
    background: currentColor;
  }
</style>
</head>
<body>
<main class="card-set">

  <section class="card card--light card--front-light">
    <div class="contact">
      <h1 class="contact__name">Derek <span class="contact__surname">Walsh</span></h1>
      <p class="contact__title">CEO</p>
      <div class="contact__rule"></div>
      <ul class="contact__details">
        <li>614-208-3917</li>
        <li>email@homebridle-example.com</li>
        <li>48 Birchfield Court, Suite 314,<br>Marlow, OH 43952</li>
        <li>NMLS 61947</li>
      </ul>
    </div>
    <p class="company-license">Company NMLS 472815</p>
    <div class="wordmark wordmark--small"><span class="wordmark__dot"></span>HomeBridle</div>
  </section>

  <section class="card card--blue card--front-blue">
    <div class="contact">
      <h1 class="contact__name">Derek <span class="contact__surname">Walsh</span></h1>
      <p class="contact__title">CEO</p>
      <div class="contact__rule"></div>
      <ul class="contact__details">
        <li>614-208-3917</li>
        <li>email@homebridle-example.com</li>
        <li>48 Birchfield Court, Suite 314,<br>Marlow, OH 43952</li>
        <li>NMLS 61947</li>
      </ul>
    </div>
    <p class="company-license">Company NMLS 472815</p>
    <div class="wordmark wordmark--small"><span class="wordmark__dot"></span>HomeBridle</div>
  </section>

  <section class="card card--light card--back-light">
    <div class="wordmark wordmark--large"><span class="wordmark__dot"></span>HomeBridle</div>
  </section>

  <section class="card card--blue card--back-blue">
    <div class="wordmark wordmark--large"><span class="wordmark__dot"></span>HomeBridle</div>
  </section>

</main>
</body>
</html>
```